Custom Manufacturing Job Shop

We are looking for a business card design for Tall Oak Fabrication Inc. Tall Oak is a family owned business that manufactures any custom product to fit a customers needs, whether it is custom 1 piece or production parts, we truly take on projects that others just cant do. to help in your design go to www.talloakfab.example for a more in depth idea. we have the following capabilities that we would like to see on the card somewhere...maybe on the back of a 2 sided card? we are fully open to ideas.
Machining
• Fabrication
• Millwork
• Maintenance
• Laser Cutting
• Precision Forming
Engineering
Blasting/Painting

No matter how big or small, We literally do it all

preferably black or darker cards but we don't mind to see some color if you see a better fit. we are interested in looking at anything that catches attention.
I have attached our logo, if it is needed in a different file type please let me know and I will send it to you if I can. maybe adding some type of drawing or dimensional lines would be something to add?? just throwing ideas out there....

Reason: I added one of our shredder designs and would like to see a few more cards if possible using this. any questions please don't hesitate to ask!!

Target Market(s)

anyone looking for design/manufacturing/machining whether it is custom 1 off parts or production.

Industry/Entity Type

Business

Contact Information for Business Card

preferably darker shades, but also not opposed to some color in the same sense....not too bright

Font styles to use
Serif
Sans Serif

Requirements
Must have
• Dell Marwick
• Direct:555-213-7790
• Cell:555-348-1162
• Fax: 555-907-4425
• 42 Quarry Lane
• Ashford Hollow, ST 00000
• I also would request having it in a format I can give to the company making the business cards to edit names/numbers etc. for the entire staff.
Nice to have
• drafting lines? we are open to almost anything....
Should not have
• exotic colors

```html
<!DOCTYPE html>
<html lang="en">
<head>
<meta charset="utf-8">
<title>Tall Oak Fabrication Inc. – Business Card</title>
<link rel="stylesheet" href="https://fonts.googleapis.com/css2?family=Lato:wght@300;400;700;900&display=swap">
<style>
  :root {
    --bg: #d9d9d9;
    --card-white: #ffffff;
    --card-dark: #4a4a4a;
    --band-light: #c4c4c4;
    --ink-dark: #575757;
    --ink-mid: #8a8a8a;
    --ink-light: #ffffff;
    --ink-soft: #d0d0d0;
  }
  * { box-sizing: border-box; margin: 0; padding: 0; }
  html, body {
    width: 1200px; height: 926px; overflow: hidden;
    background: var(--bg);
    font-family: "Lato", Arial, sans-serif;
  }
  .sheet { position: relative; width: 1200px; height: 926px; }
  .card {
    position: absolute; left: 250px; width: 700px; height: 400px;
    overflow: hidden;
    box-shadow: 0 6px 18px rgba(0,0,0,.18);
  }
  .card--back { top: 43px; background: var(--card-dark); }
  .card--front { top: 483px; background: var(--card-white); }
  .card__shape { position: absolute; inset: 0; width: 700px; height: 400px; }

  .brand {
    position: absolute; left: 0; right: 0;
    display: flex; flex-direction: column; align-items: center;
  }
  .brand__row { display: flex; align-items: center; gap: 16px; }
  .brand__dot { width: 26px; height: 26px; border-radius: 50%; }
  .brand__name {
    font-weight: 900; font-size: 66px; letter-spacing: 2px; line-height: 1;
  }
  .brand__site {
    margin-top: 10px; font-weight: 400; font-size: 18px; letter-spacing: 5px;
  }
  .card--back .brand { top: 140px; }
  .card--back .brand__name { color: var(--ink-light); }
  .card--back .brand__dot { background: var(--ink-light); }
  .card--back .brand__site { color: var(--ink-soft); }

  .card--front .brand { top: 62px; }
  .card--front .brand__name { color: var(--ink-dark); }
  .card--front .brand__dot { background: var(--ink-dark); }
  .card--front .brand__site { color: var(--ink-mid); }

  .contact {
    position: absolute; left: 0; right: 0; top: 262px;
    color: var(--ink-light); text-align: center;
  }
  .contact__name {
    font-size: 30px; letter-spacing: 2px; font-weight: 300; text-transform: uppercase;
  }
  .contact__name strong { font-weight: 700; }
  .contact__lines {
    margin-top: 18px; font-size: 15px; letter-spacing: 1.5px; text-transform: uppercase;
    line-height: 1.8;
  }
  .contact__lines span + span { margin-left: 30px; }
</style>
</head>
<body>
<main class="sheet">

  <section class="card card--back" aria-label="Card back">
    <div class="brand">
      <div class="brand__row">
        <span class="brand__name">TALL OAK</span>
        <span class="brand__dot"></span>
      </div>
      <span class="brand__site">TALLOAKFAB.EXAMPLE</span>
    </div>
  </section>

  <section class="card card--front" aria-label="Card front">
    <svg class="card__shape" viewBox="0 0 700 400" aria-hidden="true">
      <path d="M0,250 C200,232 430,196 700,178 L700,400 L0,400 Z" fill="var(--band-light)"/>
      <path d="M0,262 C200,244 430,208 700,190 L700,400 L0,400 Z" fill="var(--card-dark)"/>
      <path d="M336,226 L350,208 L364,222 Z" fill="var(--card-dark)"/>
    </svg>
    <div class="brand">
      <div class="brand__row">
        <span class="brand__name">TALL OAK</span>
        <span class="brand__dot"></span>
      </div>
      <span class="brand__site">TALLOAKFAB.EXAMPLE</span>
    </div>
    <div class="contact">
      <p class="contact__name">Dell <strong>Marwick</strong></p>
      <p class="contact__lines">
        <span>Direct:555-213-7790</span><span>Cell:555-348-1162</span><span>Fax: 555-907-4425</span><br>
        <span>42 Quarry Lane, Ashford Hollow, ST 00000</span>
      </p>
    </div>
  </section>

</main>
</body>
</html>
```